VELNA BROCADE

Project name: “Velna Brocade” website
Objective: To create an elegant website,
intuitive and responsive to present this
what is “Velna Brocade”
See attached specifications.

```html
<!DOCTYPE html>
<html lang="en">
<head>
<meta charset="utf-8">
<title>Velna Brocade</title>
<link href="https://fonts.googleapis.com/css2?family=Playfair+Display:wght@500;600;700&family=Inter:wght@400;500;600&display=swap" rel="stylesheet">
<style>
:root{
  --gold:#c9a55a;
  --gold-dark:#b38f45;
  --ink:#1f1f1f;
  --text:#555;
  --muted:#8a8a8a;
  --light:#f5f5f5;
  --white:#fff;
  --line:#e4e4e4;
  --footer:#1c1c1c;
}
*{box-sizing:border-box;margin:0;padding:0}
html,body{width:1200px;height:4908px;overflow:hidden}
body{font-family:'Inter',sans-serif;color:var(--text);background:var(--white);position:relative}
section,header,footer{position:absolute;left:0;width:1200px}
h2.section-title{font-family:'Playfair Display',serif;font-weight:600;font-size:50px;color:var(--ink);text-align:center}
.section-sub{text-align:center;font-size:15px;color:var(--muted);margin-top:12px}

/* hero */
.hero{top:0;height:660px}
.hero-photo{position:absolute;inset:0;background:linear-gradient(180deg,#1a2229 0%,#2c3437 45%,#3b3a33 75%,#1e201f 100%)}
.hero-glow{position:absolute;left:440px;top:170px;width:460px;height:300px;background:radial-gradient(ellipse at center,rgba(230,180,110,.35),rgba(0,0,0,0) 70%)}
.nav{position:absolute;top:0;left:0;width:1200px;height:44px;display:flex;align-items:center;justify-content:space-between;padding:0 112px}
.brand{font-family:'Playfair Display',serif;font-weight:600;font-size:19px;color:var(--gold)}
.nav-links{display:flex;gap:26px;list-style:none}
.nav-links li{color:var(--white);font-size:13px;font-weight:500}
.hero-actions{position:absolute;top:442px;left:0;width:1200px;display:flex;justify-content:center;gap:22px}
.btn{display:inline-block;font-size:13px;font-weight:600;padding:11px 30px;border-radius:3px}
.btn-gold{background:var(--gold);color:var(--white)}
.btn-outline{border:1.5px solid var(--white);color:var(--white)}

/* about */
.about{top:660px;height:660px}
.about .section-title{margin-top:58px}
.about-photo{position:absolute;left:122px;top:180px;width:460px;height:282px;border-radius:4px;background:linear-gradient(135deg,#d8d3cc,#a9a29b 60%,#7d756e)}
.about-body{position:absolute;left:622px;top:182px;width:460px}
.about-body h3{font-family:'Playfair Display',serif;font-size:24px;color:var(--ink);font-weight:600;margin-bottom:16px}
.about-body p{font-size:14px;line-height:1.6;margin-bottom:16px}
.stats{display:grid;grid-template-columns:1fr 1fr;row-gap:18px;margin-top:6px}
.stat-num{font-family:'Playfair Display',serif;font-size:28px;color:var(--gold)}
.stat-label{font-size:12px;color:var(--text);margin-top:2px}

/* services */
.services{top:1320px;height:520px;background:var(--light)}
.services .section-title{margin-top:56px}
.service-grid{position:absolute;top:200px;left:118px;width:964px;display:grid;grid-template-columns:repeat(4,1fr);gap:24px}
.service-card{background:var(--white);height:310px;padding:40px 24px;text-align:center;box-shadow:0 3px 14px rgba(0,0,0,.07);border-radius:4px}
.service-icon{width:64px;height:64px;border-radius:50%;background:var(--gold);margin:0 auto 26px;display:flex;align-items:center;justify-content:center}
.service-card h3{font-family:'Playfair Display',serif;font-size:20px;color:var(--ink);font-weight:600;margin-bottom:12px}
.service-card p{font-size:13px;line-height:1.55}

/* portfolio */
.portfolio{top:1840px;height:1430px}
.portfolio .section-title{margin-top:72px}
.gallery{position:absolute;top:220px;left:90px;width:1016px;display:grid;grid-template-columns:1fr 1fr;gap:24px 20px}
.tile{height:276px;border-radius:4px}
.t1{background:linear-gradient(135deg,#7c5a3f,#d9d6cf 55%,#5d8aa5)}
.t2{background:linear-gradient(135deg,#6d9bc9,#f1efe9 50%,#4d7a4f)}
.t3{background:linear-gradient(135deg,#7fb0df,#f2eee8 45%,#4aa3c4)}
.t4{background:linear-gradient(135deg,#8fb8de,#efefef 50%,#3f9ec7)}
.t5{background:linear-gradient(135deg,#3b3531,#d7cec4 50%,#9a5a34)}
.t6{background:linear-gradient(135deg,#eaeae8,#a3a4a2 50%,#2c2c2c)}
.t7{background:linear-gradient(135deg,#c0662b,#f1ede6 50%,#6f7b5a)}
.t8{background:linear-gradient(135deg,#f4f4f2,#cfcdc8 50%,#3a3a3a)}

/* testimonials */
.testimonials{top:3270px;height:760px;background:var(--light)}
.testimonials .section-title{margin-top:120px}
.quote-grid{position:absolute;top:250px;left:90px;width:1016px;display:grid;grid-template-columns:repeat(3,1fr);gap:26px}
.quote-card{background:var(--white);border-left:4px solid var(--gold);height:290px;padding:34px 30px;box-shadow:0 3px 14px rgba(0,0,0,.06)}
.quote-card p{font-size:14px;line-height:1.6;font-style:italic;color:var(--text)}
.author{display:flex;align-items:center;gap:14px;margin-top:28px}
.avatar{width:48px;height:48px;border-radius:50%;background:var(--gold);color:var(--white);font-size:14px;font-weight:600;display:flex;align-items:center;justify-content:center}
.author-name{font-family:'Playfair Display',serif;font-size:15px;font-weight:600;color:var(--ink)}
.author-role{font-size:11px;color:var(--muted);margin-top:2px}

/* contact */
.contact{top:4030px;height:690px}
.contact .section-title{margin-top:60px}
.contact-form{position:absolute;left:232px;top:222px;width:200px}
.field{margin-bottom:22px}
.field label{display:block;font-size:12px;font-weight:600;color:var(--ink);margin-bottom:8px}
.field .input{height:40px;border:1px solid var(--line);border-radius:3px;font-size:12px;color:#b5b5b5;padding:12px}
.field .textarea{height:110px}
.contact-form .btn{margin-top:4px;padding:12px 40px}
.info-card{position:absolute;left:622px;top:240px;width:478px;height:440px;background:var(--white);box-shadow:0 3px 16px rgba(0,0,0,.08);border-radius:4px;padding:30px}
.info-card h3{font-family:'Playfair Display',serif;font-size:20px;color:var(--ink);font-weight:600;padding-bottom:14px;border-bottom:1px solid var(--line);margin-bottom:20px}
.info-row{display:flex;gap:16px;margin-bottom:18px}
.info-row svg{flex:none;margin-top:2px}
.info-row h4{font-size:13px;color:var(--ink);font-weight:600;margin-bottom:4px}
.info-row p{font-size:12px;line-height:1.55}
.follow{border-top:1px solid var(--line);padding-top:14px}
.follow h4{font-size:13px;color:var(--ink);font-weight:600;margin-bottom:12px}
.social{display:flex;gap:12px}
.social span{width:36px;height:36px;border-radius:50%;background:var(--gold)}

/* footer */
.site-footer{top:4720px;height:188px;background:var(--footer);color:#bdbdbd}
.footer-cols{position:absolute;top:26px;left:98px;width:1004px;display:grid;grid-template-columns:260px 260px 260px 1fr}
.footer-cols h4{font-family:'Playfair Display',serif;font-size:15px;color:var(--white);font-weight:600;margin-bottom:12px}
.footer-cols .brand{font-size:20px;display:block;margin-bottom:10px}
.footer-cols p,.footer-cols li{font-size:12px;line-height:1.6;list-style:none}
.newsletter{display:flex;margin-top:10px}
.newsletter .email{width:180px;height:32px;background:#2c2c2c;font-size:11px;color:#8c8c8c;padding:9px 10px;border-radius:3px 0 0 3px}
.newsletter .go{width:40px;height:32px;background:var(--gold);border-radius:0 3px 3px 0;display:flex;align-items:center;justify-content:center}
.copyright{position:absolute;bottom:0;left:0;width:1200px;height:36px;border-top:1px solid #333;text-align:center;font-size:11px;line-height:36px;color:#999}
</style>
</head>
<body>

<header class="hero">
  <div class="hero-photo" role="img" aria-label="Modern two-storey luxury house at dusk with lit glass facade and trees"></div>
  <div class="hero-glow"></div>
  <nav class="nav">
    <span class="brand">Velna Brocade</span>
    <ul class="nav-links"><li>Home</li><li>About</li><li>Services</li><li>Gallery</li><li>Testimonials</li><li>Contact</li></ul>
  </nav>
  <div class="hero-actions">
    <span class="btn btn-gold">Learn More</span>
    <span class="btn btn-outline">Contact Us</span>
  </div>
</header>

<section class="about">
  <h2 class="section-title">About Velna Brocade</h2>
  <p class="section-sub">Where Vision Meets Value</p>
  <div class="about-photo" role="img" aria-label="Small model house with a key on a table"></div>
  <div class="about-body">
    <h3>Curating Excellence in Real Estate</h3>
    <p>Velna Brocade is a distinguished property and land holding company dedicated to acquiring, managing, and developing premium estates and development parcels across prime locations.</p>
    <p>With a portfolio of carefully selected properties, we represent the intersection of luxury, investment opportunity, and visionary development. Our commitment to excellence ensures that every property in our portfolio meets the highest standards of quality and potential.</p>
    <div class="stats">
      <div><div class="stat-num">250+</div><div class="stat-label">Properties Managed</div></div>
      <div><div class="stat-num">15+</div><div class="stat-label">Years Experience</div></div>
      <div><div class="stat-num">98%</div><div class="stat-label">Client Satisfaction</div></div>
      <div><div class="stat-num">$2B+</div><div class="stat-label">Assets Under Management</div></div>
    </div>
  </div>
</section>

<section class="services">
  <h2 class="section-title">Our Services</h2>
  <p class="section-sub">Comprehensive Real Estate Solutions</p>
  <div class="service-grid">
    <article class="service-card">
      <div class="service-icon"><svg width="26" height="26" viewBox="0 0 24 24" fill="none" stroke="#fff" stroke-width="2"><path d="M3 20h18M5 20V10l7-5 7 5v10"/></svg></div>
      <h3>Land Acquisition</h3>
      <p>Strategic acquisition of premium land parcels in high-growth areas with exceptional development potential.</p>
    </article>
    <article class="service-card">
      <div class="service-icon"><svg width="26" height="26" viewBox="0 0 24 24" fill="none" stroke="#fff" stroke-width="2"><rect x="5" y="3" width="14" height="18"/><path d="M9 7h2M13 7h2M9 11h2M13 11h2M10 21v-4h4v4"/></svg></div>
      <h3>Property Holding</h3>
      <p>Expert management and stewardship of premium real estate assets for optimal long-term value appreciation.</p>
    </article>
    <article class="service-card">
      <div class="service-icon"><svg width="26" height="26" viewBox="0 0 24 24" fill="#fff"><path d="M12 3l9 8h-3v9h-4v-6h-4v6H6v-9H3z"/></svg></div>
      <h3>Estate Management</h3>
      <p>Comprehensive property management services ensuring impeccable maintenance and enhanced property value.</p>
    </article>
    <article class="service-card">
      <div class="service-icon"><svg width="26" height="26" viewBox="0 0 24 24" fill="none" stroke="#fff" stroke-width="2"><path d="M3 20h18M4 16l5-5 4 3 7-7M15 7h5v5"/></svg></div>
      <h3>Development Advisory</h3>
      <p>Strategic consulting on development projects, zoning and maximizing property potential and ROI.</p>
    </article>
  </div>
</section>

<section class="portfolio">
  <h2 class="section-title">Our Portfolio</h2>
  <p class="section-sub">A Selection of Premium Properties</p>
  <div class="gallery">
    <div class="tile t1" role="img" aria-label="Modern villa with wood cladding and pool"></div>
    <div class="tile t2" role="img" aria-label="White modern house surrounded by palms"></div>
    <div class="tile t3" role="img" aria-label="White modern villa with blue pool"></div>
    <div class="tile t4" role="img" aria-label="Contemporary white house beside a pool"></div>
    <div class="tile t5" role="img" aria-label="Living room interior with wood and concrete"></div>
    <div class="tile t6" role="img" aria-label="Modern house facade with timber panels"></div>
    <div class="tile t7" role="img" aria-label="Classic white house with autumn trees"></div>
    <div class="tile t8" role="img" aria-label="Bright white kitchen with bar stools"></div>
  </div>
</section>

<section class="testimonials">
  <h2 class="section-title">Client Testimonials</h2>
  <p class="section-sub">What Our Clients Say</p>
  <div class="quote-grid">
    <article class="quote-card">
      <p>"Velna Brocade transformed our land investment strategy. Their expertise in identifying premium parcels and managing properties is unmatched. A truly professional team."</p>
      <div class="author"><div class="avatar">EF</div><div><div class="author-name">Elden Farrow</div><div class="author-role">Private Investor</div></div></div>
    </article>
    <article class="quote-card">
      <p>"Working with Velna Brocade has been exceptional. They don't just manage properties; they create value. Their attention to detail and strategic vision is impressive."</p>
      <div class="author"><div class="avatar">MO</div><div><div class="author-name">Mira Okafor</div><div class="author-role">Real Estate Developer</div></div></div>
    </article>
    <article class="quote-card">
      <p>"The level of professionalism and market insight Velna Brocade brings is outstanding. They helped us acquire and develop properties that exceeded our expectations."</p>
      <div class="author"><div class="avatar">TR</div><div><div class="author-name">Tobias Renn</div><div class="author-role">Investment Fund Manager</div></div></div>
    </article>
  </div>
</section>

<section class="contact">
  <h2 class="section-title">Get In Touch</h2>
  <p class="section-sub">Let's Discuss Your Real Estate Goals</p>
  <form class="contact-form">
    <div class="field"><label>Full Name</label><div class="input">John Doe</div></div>
    <div class="field"><label>Email Address</label><div class="input">john@example.com</div></div>
    <div class="field"><label>Phone Number</label><div class="input">+1 (555) 000-0000</div></div>
    <div class="field"><label>Message</label><div class="input textarea">Tell us about your needs...</div></div>
    <span class="btn btn-gold">Send Message</span>
  </form>
  <aside class="info-card">
    <h3>Contact Information</h3>
    <div class="info-row">
      <svg width="18" height="18" viewBox="0 0 24 24" fill="#c9a55a"><path d="M12 2a7 7 0 00-7 7c0 5 7 13 7 13s7-8 7-13a7 7 0 00-7-7zm0 9.5A2.5 2.5 0 1112 6.5a2.5 2.5 0 010 5z"/></svg>
      <div><h4>Address</h4><p>48 Linden Crescent, Suite 210<br>Harborview, HV 20417</p></div>
    </div>
    <div class="info-row">
      <svg width="18" height="18" viewBox="0 0 24 24" fill="#c9a55a"><path d="M6.6 10.8a15 15 0 006.6 6.6l2.2-2.2a1 1 0 011-.25 11.4 11.4 0 003.6.6 1 1 0 011 1V20a1 1 0 01-1 1A17 17 0 013 4a1 1 0 011-1h3.5a1 1 0 011 1c0 1.25.2 2.45.6 3.6a1 1 0 01-.25 1z"/></svg>
      <div><h4>Phone</h4><p>+1 (555) 010-2486</p></div>
    </div>
    <div class="info-row">
      <svg width="18" height="18" viewBox="0 0 24 24" fill="#c9a55a"><path d="M3 5h18v14H3zm2 2v.5l7 4.5 7-4.5V7z"/></svg>
      <div><h4>Email</h4><p>hello@velnabrocade.com</p></div>
    </div>
    <div class="info-row">
      <svg width="18" height="18" viewBox="0 0 24 24" fill="#c9a55a"><path d="M12 2a10 10 0 100 20 10 10 0 000-20zm1 10.4l3.5 2-1 1.7L11 13V6h2z"/></svg>
      <div><h4>Business Hours</h4><p>Monday - Friday: 9:00 AM - 6:00 PM<br>Saturday: 10:00 AM - 4:00 PM<br>Sunday: Closed</p></div>
    </div>
    <div class="follow">
      <h4>Follow Us</h4>
      <div class="social"><span></span><span></span><span></span><span></span></div>
    </div>
  </aside>
</section>

<footer class="site-footer">
  <div class="footer-cols">
    <div>
      <span class="brand">Velna Brocade</span>
      <p>Premium property and land holding company dedicated to excellence in real estate acquisition and management.</p>
    </div>
    <div>
      <h4>Quick Links</h4>
      <ul><li>About Us</li><li>Services</li><li>Portfolio</li><li>Testimonials</li></ul>
    </div>
    <div>
      <h4>Services</h4>
      <ul><li>Land Acquisition</li><li>Property Holding</li><li>Estate Management</li><li>Development Advisory</li></ul>
    </div>
    <div>
      <h4>Newsletter</h4>
      <p>Subscribe for property updates and market insights.</p>
      <div class="newsletter"><div class="email">Your email</div><div class="go"><svg width="12" height="12" viewBox="0 0 24 24" fill="#fff"><path d="M2 21l21-9L2 3v7l15 2-15 2z"/></svg></div></div>
    </div>
  </div>
  <div class="copyright">© 2024 Velna Brocade. All rights reserved. | Privacy Policy | Terms of Service</div>
</footer>

</body>
</html>
```